Bramwell Builders Web Site / Business Cards

Construction Company that specializes in Water and Fire Damage, Residential ReModels, Landscaping and Building ADU (Accessory Dwelling Unit)

Growing and changing families often need additional space, and a remodeling project can often provide that. Adding a new area, or repurposing an existing one can satisfy this requirement.

Other times, homeowners want to update the look in their kitchen or bathroom with more than just a change of cabinetry or vanity doors and drawers. Whatever your needs are, Bramwell Builders has skilled workers who are bonded and insured, and ready to make your dreams and visions a reality.

Target Market(s)

Home Owners

Industry/Entity Type

Construction Company

Contact Information for Business Card

Center Logo with our information on the corners

Back side to be Logo Only
Contact Info
SBRQ License # 5820914
info@bramwellbuildersca.example
www.bramwellbuildersca.example

Coding

Coded - Design and coding required

Number of Pages Required

5+ page

Font styles to use
Serif
Sans Serif

Requirements
Must have
• Using our Logo Colors
Home
About Us
Services
Projects / Portfolio
Contact Us
Nice to have
• Colors matching our Logo
Should not have
• Black because it doesnt match our logo

```html
<!DOCTYPE html>
<html lang="en">
<head>
<meta charset="utf-8">
<title>Bramwell Builders</title>
<link href="https://fonts.googleapis.com/css2?family=Roboto:wght@400;500;700;900&display=swap" rel="stylesheet">
<style>
:root{
  --orange:#f15a22;
  --orange-deep:#c8370f;
  --dark:#7a2f12;
  --dark-2:#5e2410;
  --ink:#3a1c10;
  --text:#5a4a42;
  --white:#fff;
  --line:#eadfd8;
}
*{margin:0;padding:0;box-sizing:border-box}
html,body{width:1200px;height:4448px;overflow:hidden}
body{position:relative;font-family:'Roboto',Arial,sans-serif;color:var(--ink);background:var(--white)}
.layer{position:absolute;left:0;top:0}
.abs{position:absolute}
.center{left:0;width:1200px;text-align:center}
.topbar{top:0;height:33px;left:0;width:1200px;color:#fff;font-size:13px}
.topbar span{position:absolute;top:9px}
.nav{top:33px;height:67px;left:0;width:1200px;font-size:15px;font-weight:500}
.nav a{position:absolute;top:0;height:67px;line-height:67px;color:var(--ink);text-decoration:none;padding:0 20px;border-right:1px solid var(--line)}
.nav a.active{color:var(--orange)}
.nav .quote{background:var(--orange);color:#fff;border:none;font-size:12px;font-weight:700;width:156px;text-align:center}
.logo-badge{left:500px;top:0;width:200px;height:152px;border-radius:0 0 100px 100px;background:#fff;text-align:center}
.brand{font-weight:700;color:var(--ink);letter-spacing:1px}
.brand .sq{display:inline-block;width:12px;height:12px;background:var(--orange);vertical-align:middle;margin-right:8px}
.hero-title{top:306px;font-size:46px;font-weight:700;color:#fff}
.hero-text{top:370px;left:300px;width:600px;text-align:center;color:#fff;font-size:16px;line-height:27px;font-weight:500}
.btn{display:block;background:var(--orange);color:#fff;text-align:center;font-weight:700;border-radius:25px;text-decoration:none}
.h2{font-size:38px;font-weight:700;color:var(--ink)}
.para{font-size:14px;line-height:29px;color:var(--text)}
.feature{font-size:15px;font-weight:500;line-height:23px;color:var(--ink)}
.svc-label{font-size:17px;font-weight:700;color:#fff}
.why h3{font-size:17px;font-weight:700;color:#fff;text-align:center}
.why p{font-size:15px;line-height:22px;color:#fff;text-align:center}
.quote-card{font-size:13.5px;line-height:26px;color:var(--text);text-align:center}
.name{font-size:15px;font-weight:700;text-align:center}
.name small{font-size:10px;font-weight:400;color:var(--text)}
.stars{color:#f5b400;font-size:13px;text-align:center;letter-spacing:1px}
.foot{color:#fff}
.foot h4{font-size:16px;font-weight:700}
.foot .lbl{font-size:12px;font-weight:700}
.foot .val{font-size:13px;line-height:18px}
.foot ul{list-style:none;font-size:13px;line-height:26px}
</style>
</head>
<body>
<svg class="layer" width="1200" height="4448" viewBox="0 0 1200 4448">
  <defs>
    <linearGradient id="kitchen" x1="0" y1="0" x2="1" y2="1">
      <stop offset="0" stop-color="#d9d3c8"/><stop offset=".5" stop-color="#bfb3a0"/><stop offset="1" stop-color="#8a7a68"/>
    </linearGradient>
    <linearGradient id="house" x1="0" y1="0" x2="0" y2="1">
      <stop offset="0" stop-color="#8a3a1c"/><stop offset="1" stop-color="#5e2410"/>
    </linearGradient>
    <linearGradient id="why" x1="0" y1="0" x2="1" y2="1">
      <stop offset="0" stop-color="#f26a2a"/><stop offset=".6" stop-color="#e4501c"/><stop offset="1" stop-color="#b8330f"/>
    </linearGradient>
    <linearGradient id="foot" x1="0" y1="0" x2="0" y2="1">
      <stop offset="0" stop-color="#7a2f12"/><stop offset="1" stop-color="#5e2410"/>
    </linearGradient>
    <linearGradient id="g1" x1="0" y1="0" x2="0" y2="1"><stop offset="0" stop-color="#d9cdb8"/><stop offset="1" stop-color="#6f6a5c"/></linearGradient>
    <linearGradient id="g2" x1="0" y1="0" x2="0" y2="1"><stop offset="0" stop-color="#7f7fa8"/><stop offset=".6" stop-color="#8d7f7a"/><stop offset="1" stop-color="#4b5a3a"/></linearGradient>
    <linearGradient id="g3" x1="0" y1="0" x2="0" y2="1"><stop offset="0" stop-color="#3b7fd1"/><stop offset=".6" stop-color="#8a5a50"/><stop offset="1" stop-color="#4f7a34"/></linearGradient>
    <linearGradient id="g4" x1="0" y1="0" x2="0" y2="1"><stop offset="0" stop-color="#2f8ad8"/><stop offset=".5" stop-color="#c9b04a"/><stop offset="1" stop-color="#2f7a3a"/></linearGradient>
    <linearGradient id="g5" x1="0" y1="0" x2="0" y2="1"><stop offset="0" stop-color="#7aa6d4"/><stop offset=".6" stop-color="#8b8f94"/><stop offset="1" stop-color="#4f7a3a"/></linearGradient>
  </defs>

  <rect x="0" y="0" width="1200" height="33" fill="var(--dark)"/>

  <g role="img" aria-label="Bright white kitchen with marble island, pendant lights and steel fridge">
    <rect x="0" y="100" width="1200" height="690" fill="url(#kitchen)"/>
  </g>
  <rect x="281" y="285" width="638" height="259" fill="rgba(90,70,58,.6)"/>
  <polygon points="0,792 600,680 1200,760 1200,800 0,800" fill="var(--orange)"/>
  <polygon points="0,800 600,698 1200,778 1200,800" fill="#fff"/>
  <rect x="0" y="795" width="1200" height="20" fill="#fff"/>

  <g fill="var(--orange)">
    <polygon points="172,1009 210,1031 210,1075 172,1097 134,1075 134,1031"/>
    <polygon points="436,1009 474,1031 474,1075 436,1097 398,1075 398,1031"/>
    <polygon points="678,1009 716,1031 716,1075 678,1097 640,1075 640,1031"/>
    <polygon points="919,1009 957,1031 957,1075 919,1097 881,1075 881,1031"/>
  </g>
  <g fill="none" stroke="#fff" stroke-width="3">
    <circle cx="172" cy="1048" r="14"/><path d="M164 1062 l-4 16 12-6 12 6-4-16"/>
    <path d="M418 1056 l12-12 12 8 12-12 8 8-20 20-12-8-8 8z"/>
    <circle cx="678" cy="1042" r="10"/><path d="M660 1075 v-10 h36 v10 M678 1052 v13"/>
    <circle cx="919" cy="1040" r="9"/><path d="M900 1075 q19-30 38 0"/>
  </g>

  <polygon points="0,1302 600,1228 1200,1302 1200,1316 600,1240 0,1316" fill="var(--orange)"/>
  <g role="img" aria-label="Dusk photo of a brick family home behind the services diagram">
    <polygon points="0,1316 600,1240 1200,1316 1200,1920 600,1848 0,1920" fill="url(#house)"/>
  </g>
  <line x1="510" y1="1390" x2="575" y2="1390" stroke="#fff" stroke-width="1.5"/>
  <line x1="625" y1="1390" x2="690" y2="1390" stroke="#fff" stroke-width="1.5"/>
  <circle cx="587" cy="1390" r="5" fill="var(--orange)"/><circle cx="600" cy="1390" r="6" fill="var(--orange)"/><circle cx="613" cy="1390" r="5" fill="var(--orange)"/>
  <path d="M318 1920 V1860 A282 310 0 0 1 882 1860 V1920" fill="none" stroke="#c9a898" stroke-width="10"/>
  <g fill="none" stroke="var(--orange)" stroke-width="3">
    <polyline points="210,1515 370,1515 451,1594"/>
    <polyline points="115,1617 262,1617 361,1680"/>
    <polyline points="100,1727 250,1727 321,1801"/>
    <polyline points="515,1490 665,1490 591,1549"/>
    <polyline points="975,1515 825,1515 734,1597"/>
    <polyline points="1075,1620 920,1620 827,1687"/>
    <polyline points="1100,1753 940,1753 858,1798"/>
  </g>
  <g fill="#fff" stroke="var(--orange)" stroke-width="5">
    <circle cx="321" cy="1801" r="40"/><circle cx="361" cy="1680" r="40"/><circle cx="451" cy="1594" r="40"/>
    <circle cx="591" cy="1549" r="40"/><circle cx="734" cy="1597" r="40"/><circle cx="827" cy="1687" r="40"/><circle cx="858" cy="1798" r="40"/>
  </g>
  <g fill="none" stroke="var(--dark)" stroke-width="3">
    <path d="M305 1812 v-14 l16-12 16 12 v14z"/>
    <path d="M345 1690 v-12 l16-13 16 13 v12z M345 1696 h32"/>
    <path d="M437 1605 v-13 l14-12 14 12 v13z"/>
    <path d="M577 1562 v-16 a14 14 0 0 1 28 0 v16z M591 1540 v22"/>
    <path d="M718 1606 v-13 l16-14 16 14 v13z"/>
    <path d="M811 1700 v-16 l16-12 16 12 v16z M819 1690 h16"/>
    <path d="M844 1788 h28 v10 h-28z M856 1798 v14 h12"/>
  </g>

  <line x1="554" y1="2029" x2="646" y2="2029" stroke="var(--orange)" stroke-width="3"/>
  <g role="img" aria-label="Beige high school building with glass entrance"><rect x="114" y="2067" width="484" height="282" fill="url(#g1)"/></g>
  <g role="img" aria-label="Grey two-storey house with garage at twilight"><rect x="602" y="2067" width="486" height="282" fill="url(#g2)"/></g>
  <g role="img" aria-label="Red brick family home with garage under blue sky"><rect x="114" y="2354" width="326" height="300" fill="url(#g3)"/></g>
  <g role="img" aria-label="Yellow villa beside a river with green trees"><rect x="444" y="2354" width="313" height="300" fill="url(#g4)"/></g>
  <g role="img" aria-label="Grey stone house with gables under cloudy sky"><rect x="761" y="2354" width="327" height="300" fill="url(#g5)"/></g>

  <polygon points="0,2950 345,2858 1200,2912 1200,3362 860,3452 0,3338" fill="var(--dark)"/>
  <polygon points="0,2968 345,2882 1200,2932 1200,3345 860,3430 0,3338" fill="url(#why)"/>
  <g fill="rgba(255,255,255,.15)" stroke="rgba(255,255,255,.35)" stroke-width="2">
    <circle cx="218" cy="3131" r="36"/><circle cx="471" cy="3131" r="36"/><circle cx="725" cy="3131" r="36"/><circle cx="981" cy="3131" r="36"/>
  </g>
  <g fill="none" stroke="#fff" stroke-width="2.5">
    <rect x="204" y="3116" width="26" height="30"/><path d="M209 3124 h16 M209 3131 h16 M209 3138 h10"/>
    <path d="M460 3128 l11-10 11 10 -11 14z"/><path d="M455 3146 h32"/>
    <circle cx="725" cy="3120" r="6"/><path d="M711 3146 q14-22 28 0"/>
    <rect x="968" y="3116" width="26" height="30"/><path d="M973 3125 h16 M973 3132 h16"/>
  </g>

  <g fill="#fff" stroke="var(--line)" stroke-width="2">
    <rect x="109" y="3647" width="311" height="190" rx="12"/>
    <rect x="444" y="3647" width="311" height="190" rx="12"/>
    <rect x="777" y="3647" width="311" height="190" rx="12"/>
  </g>
  <g stroke="var(--orange)" stroke-width="3">
    <line x1="111" y1="3649" x2="210" y2="3649"/><line x1="320" y1="3649" x2="418" y2="3649"/>
    <line x1="446" y1="3649" x2="545" y2="3649"/><line x1="655" y1="3649" x2="753" y2="3649"/>
    <line x1="779" y1="3649" x2="878" y2="3649"/><line x1="988" y1="3649" x2="1086" y2="3649"/>
  </g>
  <g fill="#d8c8bf" stroke="#fff" stroke-width="4">
    <circle cx="265" cy="3647" r="45" role="img" aria-label="Client portrait"/>
    <circle cx="600" cy="3647" r="45" role="img" aria-label="Client portrait"/>
    <circle cx="932" cy="3647" r="45" role="img" aria-label="Client portrait"/>
  </g>

  <polygon points="0,4050 345,3988 1200,4082 1200,4448 0,4448" fill="var(--orange)"/>
  <polygon points="0,4068 345,4008 1200,4098 1200,4448 0,4448" fill="url(#foot)"/>
  <line x1="114" y1="4395" x2="1088" y2="4395" stroke="rgba(255,255,255,.2)"/>
  <g fill="var(--orange)">
    <path d="M374 4186 l6 0 2 5 -3 2 q3 6 8 8 l2-3 5 2 0 6 q-14 0 -20-20z"/>
    <rect x="370" y="4225" width="14" height="10"/>
    <path d="M377 4277 a6 6 0 0 1 6 6 q0 5 -6 11 q-6-6-6-11 a6 6 0 0 1 6-6z"/>
  </g>
</svg>

<div class="abs topbar">
  <span style="left:114px">f&nbsp;&nbsp;&nbsp;&nbsp;&nbsp;◎&nbsp;&nbsp;&nbsp;&nbsp;&nbsp;in</span>
  <span style="left:244px">☎ +1 555 308 2276</span>
  <span style="left:880px">✉ info@bramwellbuildersca.example</span>
</div>

<nav class="abs nav">
  <a class="active" style="left:90px;border:none">Home</a>
  <a style="left:190px">About us</a>
  <a style="left:310px">Services</a>
  <a style="left:717px">Projects</a>
  <a style="left:818px">Contact us</a>
  <a class="quote" style="left:932px">✎ GET A QUOTE</a>
</nav>
<div class="abs logo-badge">
  <div class="brand" style="margin-top:62px;font-size:22px"><span class="sq"></span>BRAMWELL</div>
  <div class="brand" style="font-size:11px;letter-spacing:4px;margin-top:4px">BUILDERS</div>
</div>

<h1 class="abs center hero-title">BRAMWELL BUILDERS</h1>
<p class="abs hero-text">Lorem ipsum dolor sit amet, consectetur adipiscing elit, sed do eiusmod tempor incididunt ut labore et dolore magna aliqua.</p>
<a class="abs btn" style="left:506px;top:458px;width:186px;height:50px;line-height:50px;font-size:16px">GET STARTED</a>

<h2 class="abs center h2" style="top:820px">WHO WE ARE</h2>
<p class="abs para" style="left:212px;top:888px;width:776px;text-align:center">We are rethoric question ran over her cheek When she reached the first hills of the Italic Mountains, she had a last view back on the skyline of her hometown Bookmarksgrove, the headline of Alphabet Village and the subline of her own road, the Line Lane.</p>
<div class="abs feature" style="left:223px;top:1030px">We've Repution For<br>Excellence</div>
<div class="abs feature" style="left:488px;top:1030px">We Build<br>Partnerships</div>
<div class="abs feature" style="left:730px;top:1030px">Guided By<br>Commitment</div>
<div class="abs feature" style="left:971px;top:1030px">A Team Of<br>Professionals</div>

<h2 class="abs center h2" style="top:1316px;color:#fff">OUR SERVICES</h2>
<div class="abs svc-label" style="left:219px;top:1480px">MOLD</div>
<div class="abs svc-label" style="left:121px;top:1582px">WATER DAMAGE</div>
<div class="abs svc-label" style="left:107px;top:1692px">FIRE DAMAGE</div>
<div class="abs svc-label" style="left:568px;top:1456px">ADUS</div>
<div class="abs svc-label" style="left:850px;top:1484px">RESTORATION</div>
<div class="abs svc-label" style="left:991px;top:1589px">REMODEL</div>
<div class="abs svc-label" style="left:924px;top:1719px">LIGHT COMMERCIAL</div>

<h2 class="abs center h2" style="top:1975px">PROJECT GALLERY</h2>
<a class="abs btn" style="left:492px;top:2703px;width:216px;height:46px;line-height:46px;font-size:14px">SEE ALL PROJECTS ➔</a>

<h2 class="abs center h2" style="top:2977px;color:#fff">WHY CHOOSE US</h2>
<div class="why">
  <div class="abs" style="left:108px;top:3188px;width:220px"><h3>CERTIFIED PERSONNEL</h3><p style="margin-top:12px">Lorem ipsum dolor sit amet, consectetur adipiscing elit, sed eiusmod tempor incididunt</p></div>
  <div class="abs" style="left:361px;top:3188px;width:220px"><h3>HIGH QUALITY WORK</h3><p style="margin-top:12px">Lorem ipsum dolor sit amet, consectetur adipiscing elit, sed eiusmod tempor incididunt</p></div>
  <div class="abs" style="left:615px;top:3188px;width:220px"><h3>PROFESSIONAL TEAM</h3><p style="margin-top:12px">Lorem ipsum dolor sit amet, consectetur adipiscing elit, sed eiusmod tempor incididunt</p></div>
  <div class="abs" style="left:871px;top:3188px;width:220px"><h3>YEARS OF EXPERIENCE</h3><p style="margin-top:12px">Lorem ipsum dolor sit amet, consectetur adipiscing elit, sed eiusmod tempor incididunt</p></div>
</div>

<h2 class="abs center" style="top:3533px;font-size:33px;font-weight:700">WHAT OUR CLIENTS SAY?</h2>
<p class="abs quote-card" style="left:135px;top:3712px;width:260px">and for all the wonderful work you and your crew are doing. Our team has nothing but good things to say - we are really fortunate to have found you for</p>
<p class="abs quote-card" style="left:470px;top:3712px;width:260px">Bramwell Builders is one of the best general contractors we've worked with. The entire team tactfully delivered a project of exceptional quality while</p>
<p class="abs quote-card" style="left:802px;top:3712px;width:260px">Lorem ipsum dolor sit consectetur adipiscing elit, sed do eiusmod tempor incididunt ut labore et dolore magna aliqua. Ut enim ad minim veniam,</p>
<div class="abs name" style="left:109px;top:3860px;width:311px">Dana Whitlow, <small>Chairman HRG</small></div>
<div class="abs name" style="left:444px;top:3860px;width:311px">Lena Marsh, <small>Project Manager</small></div>
<div class="abs name" style="left:777px;top:3860px;width:311px">Owen Prescott, <small>Chairman HRG</small></div>
<div class="abs stars" style="left:109px;top:3882px;width:311px">★★★★★</div>
<div class="abs stars" style="left:444px;top:3882px;width:311px">★★★★★</div>
<div class="abs stars" style="left:777px;top:3882px;width:311px">★★★★★</div>

<footer class="foot">
  <div class="abs" style="left:114px;top:4180px;width:200px;text-align:center">
    <div style="font-size:38px;font-weight:700;color:#fff;letter-spacing:2px">BRAMWELL</div>
    <div style="font-size:14px;font-weight:700;color:#fff;letter-spacing:6px">BUILDERS</div>
    <div style="font-size:11px;margin-top:16px">SBRQ LICENSE # 5820914</div>
    <div style="font-size:15px;margin-top:20px;letter-spacing:12px">f ✦ in ◎</div>
  </div>
  <h4 class="abs" style="left:370px;top:4140px">Our Office Address</h4>
  <div class="abs" style="left:392px;top:4184px"><div class="lbl">Phone</div><div class="val">555-308-2276</div></div>
  <div class="abs" style="left:392px;top:4222px"><div class="lbl">Email</div><div class="val">info@bramwellbuildersca.example</div></div>
  <div class="abs" style="left:392px;top:4274px;width:230px"><div class="lbl">Location</div><div class="val">412 W Orchard Lane Fairhaven, CA 90000</div></div>
  <h4 class="abs" style="left:672px;top:4140px">Company</h4>
  <ul class="abs" style="left:672px;top:4178px"><li>Home</li><li>About us</li><li>Services</li><li>Projects</li><li>Contact us</li></ul>
  <h4 class="abs" style="left:862px;top:4140px">Stil have questios?</h4>
  <p class="abs" style="left:862px;top:4185px;width:240px;font-size:12px;line-height:18px">Contact us using this form. A representative will aswer your questions as soon as possible.</p>
  <a class="abs btn" style="left:862px;top:4269px;width:198px;height:40px;line-height:40px;font-size:14px">GET IN TOUCH</a>
  <div class="abs" style="left:1008px;top:4350px;width:83px;height:20px;line-height:20px;background:#fff;color:var(--dark);border-radius:10px;font-size:11px;font-weight:700;text-align:center">▲ Go Up</div>
  <div class="abs" style="left:114px;top:4409px;font-size:13px">© 2020 Bramwell Builders | All Rights Reserved</div>
  <div class="abs" style="left:760px;top:4409px;font-size:13px">Privacy Policy &nbsp;|&nbsp; Cookie Policy &nbsp;|&nbsp; Terms Of Services</div>
</footer>
</body>
</html>
```